Magento e-commerce webdesign

We need a full e-commerce design for a company based in France. The website will sell belts (men / women).
In files, you have our logo. We made a try for a brown visit card, but it's just an idea. The brown color can be used if it looks like leather, warning it MUSN'T look like "brown shit" :)
So you are free with color but never forget we sell belts and it's both for men & women (upmarket). You can make your own colors changes on the logo (only colors).
You'll find 2 wireframes with the home page & the category page. Elements are in french. UPDATED : you have a traduction files, but it would better if you can make it in french.
Photos have to be on a white background.
Carroussel & every pictures of the wireframes area are very importants.
Target Market(s)
Men & women
Fashion peoples
Upmarket
Industry/Entity Type
It Company
Requirements
Must have
- work on the colors
- work on the pictures (carroussel, newsletter, ventes privées, services, category)
- pro & upmarket
Nice to have
- Product detail page
- Texts in french
Should not have
- Shitty brown colors

```html
<!DOCTYPE html>
<html lang="fr">
<head>
<meta charset="utf-8">
<title>Sanglora — Ceintures homme &amp; femme</title>
<link href="https://fonts.googleapis.com/css2?family=Ubuntu:wght@300;400;500;700&display=swap" rel="stylesheet">
<style>
:root{
  --page:#f3ece8;
  --page-top:#e9dfda;
  --maroon:#5b0f2b;
  --maroon-dark:#3f0a1d;
  --wine:#7a1640;
  --brown:#5a3a2c;
  --beige:#e7dcd4;
  --card-top:#cbbab0;
  --ink:#222;
  --muted:#666;
  --grey-box:#555759;
  --teal:#31c4c6;
  --magenta:#c01f6b;
  --fb:#3d5a9a;
  --tw:#7fd3ee;
  --white:#fff;
}
*{box-sizing:border-box;margin:0;padding:0}
html,body{width:827px;height:1200px;overflow:hidden}
body{position:relative;background:linear-gradient(var(--page-top),var(--page) 160px,#f6f1ee);font-family:"Ubuntu",Verdana,sans-serif;color:var(--ink)}
.abs{position:absolute}

/* header */
.brand{left:27px;top:58px;display:flex;align-items:center;gap:14px}
.brand-dot{width:26px;height:26px;border-radius:50%;background:var(--brown)}
.brand-name{font-size:50px;font-weight:400;color:var(--brown);letter-spacing:1px;line-height:1}
.search{left:632px;top:35px;width:144px;height:17px;border:1px solid #8a8380;border-radius:9px;background:var(--white);font-size:10px;color:#999;padding:2px 8px}
.search-icon{left:780px;top:34px}
.cart{left:725px;top:86px;display:flex;align-items:center;gap:8px;font-size:12px;font-weight:700}
.cart-rule{left:660px;top:110px;width:137px;height:1px;background:linear-gradient(90deg,transparent,#aaa)}
.cart-state{left:764px;top:114px;font-size:11px;font-weight:700}

/* nav */
.nav{left:27px;top:155px;width:770px;height:36px;background:linear-gradient(var(--wine),var(--maroon-dark));display:flex;align-items:center;justify-content:space-between}
.nav-main{display:flex;align-items:center;padding-left:16px;color:var(--white);font-size:12.5px;font-weight:700;gap:10px}
.nav-main .sep{width:4px;height:4px;border-radius:50%;background:var(--white)}
.nav-account{height:36px;width:175px;background:linear-gradient(#9c1f55,#6b0f37);display:flex;align-items:center;justify-content:center;gap:10px;color:var(--white);font-size:11px;font-weight:700}
.crumb{left:27px;top:192px;width:770px;height:23px;background:var(--beige);font-size:10.5px;font-weight:700;padding:5px 16px}

/* hero */
.hero{left:27px;top:236px;width:537px;height:268px;border:1px solid #d5b8a8;background:linear-gradient(90deg,#f0e4db,#fdfaf8 55%,#e9ecef);overflow:hidden}
.hero-belts{left:14px;top:14px;width:250px;height:230px;border-radius:6px;background:linear-gradient(135deg,#8a6a55,#4a3328 60%,#b08a70)}
.hero-model{left:320px;top:20px;width:200px;height:247px;border-radius:60px 60px 0 0;background:linear-gradient(#e9c9a8,#dbe3ee 60%)}
.hero-btn{left:363px;top:217px;width:156px;height:37px;border-radius:5px;background:linear-gradient(#f06aa6,var(--magenta));color:var(--white);font-size:16px;display:flex;align-items:center;justify-content:center;gap:10px}
.hero-dots{left:8px;top:249px;display:flex;gap:5px}
.hero-dots span{width:10px;height:10px;border-radius:50%;background:#111}
.hero-dots span:first-child{background:#6a5a55;box-shadow:0 0 0 2px #ccc}

/* side promos */
.promo{left:571px;width:226px;border:1px solid #777}
.newsletter{top:237px;height:83px;background:linear-gradient(#6a6c6e,var(--grey-box));padding:7px}
.newsletter h3{color:var(--white);font-size:15px;font-weight:500}
.newsletter .field{margin-top:5px;height:20px;border:2px solid #b9d47a;background:var(--white);font-size:10px;color:#888;padding:2px 4px}
.newsletter .unsub{position:absolute;left:7px;top:62px;color:var(--white);font-size:9px;font-weight:700}
.newsletter .subscribe{position:absolute;right:6px;top:60px;background:var(--maroon);color:var(--white);font-size:10px;font-weight:700;border-radius:9px;padding:3px 8px}
.ventes{top:328px;height:84px;background:linear-gradient(#44d8d8,var(--teal) 60%,#1aa6aa)}
.ventes-badge{left:10px;top:6px;width:70px;height:70px;border-radius:50%;background:#f4efe8;border:3px dashed #d8cbb8}
.ventes-title{right:18px;top:15px;color:var(--white);font-size:25px;font-weight:300;line-height:1.05;text-align:right}
.services{top:420px;height:83px;background:linear-gradient(90deg,#e44d8e,var(--magenta) 45%,#8d0f48)}
.services-photo{left:0;top:0;width:80px;height:81px;background:linear-gradient(135deg,#f0c7a0,#c98c66)}
.services-title{left:95px;top:12px;color:var(--white);font-size:25px;font-weight:300}
.services-sub{left:95px;top:46px;color:var(--white);font-size:11px;line-height:1.3}

/* products */
.product{top:528px;width:180px;height:250px;background:linear-gradient(var(--card-top),var(--beige) 50%,#efe6df);border-radius:4px 4px 0 0;padding:7px 5px}
.product-photo{width:170px;height:171px;background:var(--white);display:flex;align-items:center;justify-content:center}
.product-photo div{width:140px;height:140px;border-radius:10px}
.product p{font-size:10.5px;line-height:1.3;padding:9px 10px 0 3px;color:#222}
.product .price{position:absolute;left:8px;bottom:3px;font-size:15px}
.product .buy{position:absolute;right:0;bottom:0;width:66px;height:22px;background:#3c3c3c;color:var(--white);font-size:11px;font-weight:700;display:flex;align-items:center;justify-content:center}

/* info */
.info{top:806px;width:185px;height:99px;border:1px solid #aaa;border-radius:9px;background:var(--white)}
.info h4{display:flex;align-items:center;gap:6px;font-size:12px;font-weight:500;padding:7px 8px 5px;border-bottom:1px solid #ddd;margin:0 4px}
.info p{font-size:10.5px;font-style:italic;color:var(--muted);padding:9px 12px;line-height:1.25}
.cards{display:flex;gap:10px;padding:12px 10px}
.cards span{width:36px;height:22px;border-radius:3px}
.phone{margin:10px 12px 4px;height:22px;border:1px solid #999;border-radius:11px;display:flex;align-items:center;font-size:12px;color:#666}
.phone .flag{display:flex;width:18px;height:13px;margin:0 26px 0 8px}
.phone .flag i{flex:1}
.contact{font-size:10.5px;color:#555;text-align:center}

/* blog */
.blog{left:27px;top:928px;width:475px;height:169px;border:1px solid #ccc;border-radius:9px;background:linear-gradient(var(--white),#f1e8e2);overflow:hidden}
.blog h2{height:31px;background:linear-gradient(var(--wine),var(--maroon-dark));color:var(--white);font-size:15px;font-weight:500;padding:7px 15px}
.blog p{font-size:11px;line-height:1.3;padding:6px 15px 0;color:#222}
.blog .more{display:block;text-align:right;font-size:10px;font-weight:700;padding:4px 40px 0 0}
.social{left:511px;width:286px;height:83px;border-radius:9px;display:flex;align-items:center;gap:20px;padding-left:14px}
.social .mark{width:60px;height:60px;border-radius:8px;background:rgba(255,255,255,.85)}
.social span{color:var(--white);font-size:21px;font-style:italic;font-weight:500;line-height:1.2}
.social-fb{top:928px;background:linear-gradient(#6a86c4,var(--fb))}
.social-tw{top:1016px;background:linear-gradient(#b9ecfa,var(--tw))}

/* footer */
.footer{left:0;top:1128px;width:827px;height:72px;background:linear-gradient(#6e1a35,#4b0b1d);color:var(--white);font-size:10px;font-weight:700;display:flex;justify-content:space-between;align-items:center;padding:0 29px}
.footer nav{display:flex;gap:8px;align-items:center}
.footer nav i{width:3px;height:3px;border-radius:50%;background:var(--white)}
</style>
</head>
<body>

<header>
  <div class="abs brand"><span class="brand-name">sanglora</span><span class="brand-dot"></span></div>
  <div class="abs search">Search...</div>
  <svg class="abs search-icon" width="16" height="16" viewBox="0 0 16 16"><circle cx="6.5" cy="6.5" r="4.5" fill="none" stroke="#8aa" stroke-width="1.5"/><line x1="10" y1="10" x2="14" y2="14" stroke="#8aa" stroke-width="2"/></svg>
  <div class="abs cart">
    <svg width="26" height="18" viewBox="0 0 26 18"><path d="M1 2h4l3 10h13l3-8H7" fill="none" stroke="#222" stroke-width="2"/><path d="M8 5h15l-2 6H10z" fill="#222"/><circle cx="10" cy="16" r="1.8" fill="#222"/><circle cx="20" cy="16" r="1.8" fill="#222"/></svg>
    Panier
  </div>
  <div class="abs cart-rule"></div>
  <div class="abs cart-state">(vide)</div>

  <nav class="abs nav">
    <div class="nav-main">Homme<span class="sep"></span>Femme<span class="sep"></span>Accessories</div>
    <div class="nav-account">Mon compte <span>|</span> Parrainage</div>
  </nav>
  <div class="abs crumb">Home</div>
</header>

<section class="abs hero">
  <div class="abs hero-belts" role="img" aria-label="Ceintures en cuir à boucles ouvragées"></div>
  <div class="abs hero-model" role="img" aria-label="Femme souriante désignant les ceintures"></div>
  <div class="abs hero-btn">View Products <svg width="10" height="12" viewBox="0 0 10 12"><path d="M0 0l10 6-10 6z" fill="#fff"/></svg></div>
  <div class="abs hero-dots"><span></span><span></span><span></span><span></span><span></span></div>
</section>

<aside>
  <div class="abs promo newsletter">
    <h3>Newsletter Sign-Up:</h3>
    <div class="field">Entrez votre adresse e-mail...</div>
    <span class="unsub">Unsubscribe here</span>
    <span class="subscribe">Subscribe</span>
  </div>
  <div class="abs promo ventes">
    <div class="abs ventes-badge" role="img" aria-label="Badge -50% avec boucle de ceinture"></div>
    <div class="abs ventes-title">Vente<br>Prives</div>
  </div>
  <div class="abs promo services">
    <div class="abs services-photo" role="img" aria-label="Conseillère avec casque téléphonique"></div>
    <div class="abs services-title">Services</div>
    <div class="abs services-sub">Besoin d'aide pour choisir<br>votre ceinture ?</div>
  </div>
</aside>

<section>
  <article class="abs product" style="left:27px">
    <div class="product-photo"><div role="img" aria-label="Ceinture motif zèbre" style="background:linear-gradient(135deg,#e8e8e8,#555 50%,#ddd)"></div></div>
    <p>Lorem Ipsum is simply dummy text of the printing and typesetting industry.</p>
    <span class="price">$ 420.00</span><span class="buy">Buy Now</span>
  </article>
  <article class="abs product" style="left:223px">
    <div class="product-photo"><div role="img" aria-label="Ceinture en cuir marron" style="background:linear-gradient(135deg,#7a4a32,#4a2a1c)"></div></div>
    <p>Lorem Ipsum is simply dummy text of the printing and typesetting industry.</p>
    <span class="price">$ 420.00</span><span class="buy">Buy Now</span>
  </article>
  <article class="abs product" style="left:420px">
    <div class="product-photo"><div role="img" aria-label="Ceinture violette à boucle bijou" style="background:linear-gradient(135deg,#6a3a8a,#4a2466)"></div></div>
    <p>Lorem Ipsum is simply dummy text of the printing and typesetting industry.</p>
    <span class="price">$ 420.00</span><span class="buy">Buy Now</span>
  </article>
  <article class="abs product" style="left:616px">
    <div class="product-photo"><div role="img" aria-label="Ceinture tressée noire" style="background:linear-gradient(135deg,#555,#222)"></div></div>
    <p>Lorem Ipsum is simply dummy text of the printing and typesetting industry.</p>
    <span class="price">$ 420.00</span><span class="buy">Buy Now</span>
  </article>
</section>

<section>
  <div class="abs info" style="left:29px">
    <h4><svg width="13" height="15" viewBox="0 0 13 15"><path d="M6.5 0L13 3v5c0 3-3 6-6.5 7C3 14 0 11 0 8V3z" fill="#444"/></svg>Payment CB + Virepay:</h4>
    <div class="cards"><span style="background:#2a4a8c"></span><span style="background:#e0262e"></span><span style="background:#d11a2a"></span><span style="background:#1a3a8a"></span></div>
  </div>
  <div class="abs info" style="left:222px">
    <h4><svg width="20" height="13" viewBox="0 0 20 13"><rect x="0" y="0" width="12" height="9" fill="#222"/><path d="M12 3h4l3 3v3h-7z" fill="#222"/><circle cx="4" cy="11" r="2" fill="#222"/><circle cx="15" cy="11" r="2" fill="#222"/></svg>Livraison</h4>
    <p style="font-style:normal">It is a long established fact that a reader will be&nbsp; when looking at its layout.</p>
  </div>
  <div class="abs info" style="left:415px">
    <h4><svg width="14" height="14" viewBox="0 0 14 14"><path d="M3 0l3 3-2 2c1 2 3 4 5 5l2-2 3 3-2 3C6 14 0 8 0 3z" fill="#222"/></svg>Service Client</h4>
    <div class="phone"><span class="flag"><i style="background:#2a3f9a"></i><i style="background:#fff"></i><i style="background:#d8262e"></i></span>45 210 9876</div>
    <div class="contact">Contact our Service Center</div>
  </div>
  <div class="abs info" style="left:607px">
    <h4><svg width="12" height="16" viewBox="0 0 12 16"><circle cx="6" cy="5" r="5" fill="#444"/><path d="M2 9l-1 7 5-3 5 3-1-7z" fill="#444"/></svg>Garantie</h4>
    <p>It is a long established fact that a reader will be&nbsp; when looking at its layout.</p>
  </div>
</section>

<section>
  <div class="abs blog">
    <h2>Derniers articles du blog</h2>
    <p>Lorem Ipsum is simply dummy text of the printing and typesetting industry. Lorem Ipsum has been the industry's standard dummy text ever since the 1500s, when an unknown printer took a galley of type and scrambled it to make a type specimen book.</p>
    <span class="more">Read More</span>
    <p>It was popularised in the 1960s with the release of Typosheet sheets containing Lorem Ipsum passages, and more recently with desktop publishing software like Pagecraft including versions of Lorem Ipsum.</p>
    <span class="more">Read More</span>
  </div>
  <div class="abs social social-fb"><span class="mark"></span><span>Amisphère<br>5177+ Fans</span></div>
  <div class="abs social social-tw"><span class="mark"></span><span>Chirpline 500+<br>Followers</span></div>
</section>

<footer class="abs footer">
  <span>Copyright © 2010 sanglora.com. All Rights Reserved</span>
  <nav>CGV<i></i>CGU<i></i>Plan Du Site<i></i>Credits</nav>
</footer>

</body>
</html>
```